" A ORBALI Sistemas de Controle Industriais (ORBALI) é uma empresa brasileira cujo foco é o desenvolvimento de sistemas de análise e medição de processos industriais através da utilização de visão computacional. A ORBALI tem por objetivo fornecer ao mercado produtos e soluções para controle avançado e otimização de processos industriais utilizando análise de imagens. ****Os produtos e soluções da ORBALI realizam análises online de qualidade do processo industrial permitindo um controle imediato e continuo do processo industrial pelo cliente. Este é um conceito que pode também ser mostrado na site. O mercado alvo da ORBALI é o mercado industrial, em especial o mercado de mineração onde a ORBALI oferece analisadores online de processos industriais e projetos especiais para controles avançados de processos, promovendo para seus clientes melhorias nos seus processos e ganhos de produtividade. Dentro de seu plano estratégico a ORBALI tem como meta se tornar um dos principais fornecedores de soluções inovadoras de sistemas de visão computacional no mercado nacional e se tornar um exportador destas soluções para América do Sul e outros mercados internacionais. "

```html
<!DOCTYPE html>
<html lang="pt-BR">
<head>
<meta charset="utf-8">
<title>ORBALI — Clientes &amp; Parceiros</title>
<link href="https://fonts.googleapis.com/css2?family=Open+Sans:wght@400;600;700&family=Raleway:wght@300;400;600;700&display=swap" rel="stylesheet">
<style>
:root{
  --green:#3fae2a;
  --green-dark:#2e8f1d;
  --green-light:#7cc94f;
  --ink:#2b2b2b;
  --text:#333;
  --muted:#888;
  --line:#d9d9d9;
  --header:#2a2a2a;
  --card:#f1f1f1;
  --white:#fff;
}
*{box-sizing:border-box;margin:0;padding:0}
html,body{width:1200px;height:1200px;overflow:hidden;background:var(--white);font-family:"Open Sans",sans-serif;color:var(--text)}
.page{position:relative;width:900px;height:1200px;margin:0 auto;background:var(--white)}
.site-header{position:absolute;left:0;top:0;width:900px;height:72px;background:linear-gradient(#3a3a3a,var(--header));display:flex;align-items:center;justify-content:space-between;padding:0 40px 0 64px}
.brand{display:flex;align-items:center;gap:10px;color:var(--white);font-family:"Raleway",sans-serif;font-weight:700;font-size:30px;letter-spacing:1px}
.brand-dot{width:30px;height:30px;border-radius:50%;background:var(--green)}
.main-nav{display:flex;gap:14px;font-family:"Raleway",sans-serif;font-weight:700;font-size:10.5px;color:var(--white)}
.main-nav span{padding:5px 6px}
.main-nav .active{border:1px solid var(--white);border-radius:3px}
.hero{position:absolute;left:0;top:72px;width:900px;height:259px;overflow:hidden}
.hero-photo{position:absolute;inset:0;background:linear-gradient(120deg,#c9cdd2 0%,#8b939c 40%,#4d5660 75%,#2f363d 100%)}
.hero-circle{position:absolute;left:502px;top:0;width:360px;height:360px;border-radius:50%;background:rgba(63,174,42,.78);border:6px solid rgba(255,255,255,.35);top:-40px}
.hero-title{position:absolute;left:536px;top:100px;width:300px;color:var(--white);font-family:"Raleway",sans-serif;font-weight:700;font-size:21px;letter-spacing:.5px}
.hero-text{position:absolute;left:536px;top:140px;width:280px;color:var(--white);font-size:15px;line-height:1.45;text-align:right}
.intro{position:absolute;left:0;top:344px;width:900px;text-align:center}
.intro h1{font-family:"Raleway",sans-serif;font-weight:400;font-size:26px;color:var(--green)}
.intro p{width:700px;margin:10px auto 0;font-size:13.5px;line-height:1.6;text-align:left;color:var(--ink)}
.toggle{position:absolute;top:533px;left:0;width:900px;display:flex;justify-content:center;gap:14px}
.toggle span{width:90px;height:26px;display:flex;align-items:center;justify-content:center;font-size:9px;font-weight:600;border:1px solid var(--green);color:var(--ink)}
.toggle .on{background:var(--green);color:var(--white)}
.partners{position:absolute;top:590px;left:66px;width:768px;display:flex;justify-content:space-between}
.partner{width:110px;height:70px;background:var(--white);box-shadow:0 0 3px rgba(0,0,0,.2);display:flex;align-items:center;justify-content:center}
.partner i{display:block;width:60px;height:28px;background:#c9c9c9;border-radius:3px}
.rule{position:absolute;left:60px;width:780px;height:1px;background:var(--line)}
.section-title{position:absolute;left:0;width:900px;text-align:center;font-family:"Raleway",sans-serif;font-size:22px;color:var(--green)}
.testimonial{position:absolute;top:735px;width:370px;height:110px}
.avatar{position:absolute;left:0;top:0;width:78px;height:78px;border-radius:50%;background:radial-gradient(#e9d3c0,#b9a07f);border:3px solid var(--white);box-shadow:0 0 3px rgba(0,0,0,.25);z-index:1}
.quote{position:absolute;left:46px;top:0;width:324px;height:108px;background:var(--card);padding:10px 12px 0 46px;font-size:10px;line-height:1.45;color:#666}
.quote .who{margin-top:14px;font-weight:700;color:var(--ink)}
.quote .role{color:var(--green);font-weight:600;font-size:9px}
.contact-title{position:absolute;left:66px;top:896px;font-family:"Raleway",sans-serif;font-weight:700;font-size:32px;color:var(--green-dark)}
.contact-title span{font-weight:400;color:var(--green)}
.field{position:absolute;border:1px solid #bbb;background:var(--white);font-size:9px;color:var(--muted);padding:6px 8px}
.send{position:absolute;left:150px;top:1080px;width:80px;height:26px;background:var(--green);color:var(--white);font-size:10px;font-weight:700;display:flex;align-items:center;justify-content:center}
.info{position:absolute;top:966px;text-align:center;font-size:10px;line-height:1.45;color:var(--ink)}
.info svg{display:block;margin:0 auto 6px}
.site-footer{position:absolute;left:0;top:1118px;width:900px;height:82px;background:linear-gradient(var(--green-light),var(--green))}
.foot-nav{position:absolute;left:0;top:18px;width:900px;display:flex;justify-content:center;gap:14px;font-family:"Raleway",sans-serif;font-weight:700;font-size:9px;color:var(--white)}
.copy{position:absolute;left:0;top:48px;width:900px;text-align:center;padding-left:420px;font-size:10px;color:var(--white)}
.to-top{position:absolute;left:790px;top:12px;width:24px;height:24px;border:2px solid var(--white);border-radius:50%}
</style>
</head>
<body>
<div class="page">
  <header class="site-header">
    <div class="brand"><span class="brand-dot"></span>ORBALI</div>
    <nav class="main-nav">
      <span>HOME</span><span>A EMPRESA</span><span>TECNOLOGIA</span><span>PRODUTOS &amp; SERVIÇOS</span><span class="active">CLIENTES &amp; PARCEIROS</span><span>CONTATO</span>
    </nav>
  </header>

  <section class="hero">
    <div class="hero-photo" role="img" aria-label="Fotografia de um aperto de mãos entre dois profissionais de terno"></div>
    <div class="hero-circle"></div>
    <h2 class="hero-title">CLIENTES &amp; PARCEIROS</h2>
    <p class="hero-text">Clientes satisfeitos e geração de valor para toda a cadeia de nosso negócio é a motivação diária da ORBALI.</p>
  </section>

  <section class="intro">
    <h1>Clientes e Parceiro são nosso maior patrimônio</h1>
    <p>Oferecer soluções de alta qualidade e tecnologia para nossos clientes, fazê-los satisfeitos e manter esta satisfação é a motivação diária da ORBALI.<br>
    Para tanto contamos com parceiros que nos apoiam no nosso compromisso com a qualidade de nossas soluções, produtos e serviços.<br>
    Isto permite uma relação forte e virtuosa entre nossos Clientes, nossos Fornecedores e a ORBALI gerando valor para todos os elos.</p>
  </section>

  <div class="toggle"><span>CLIENTES</span><span class="on">PARCEIROS</span></div>

  <div class="partners">
    <div class="partner"><i></i></div><div class="partner"><i></i></div><div class="partner"><i></i></div>
    <div class="partner"><i></i></div><div class="partner"><i></i></div><div class="partner"><i></i></div>
  </div>

  <div class="rule" style="top:686px"></div>
  <h2 class="section-title" style="top:694px">Depoimentos de Clientes</h2>

  <article class="testimonial" style="left:66px">
    <div class="avatar" role="img" aria-label="Foto da cliente"></div>
    <div class="quote">Lorem ipsum dolor sit amet, consectetuer adipiscing elit. Suspendisse et justo. Praesent.
      <div class="who">Marta Lins</div><div class="role">Marketing - Nome da empresa</div></div>
  </article>
  <article class="testimonial" style="left:464px">
    <div class="avatar" role="img" aria-label="Foto da cliente"></div>
    <div class="quote">Lorem ipsum dolor sit amet, consectetuer adipiscing elit. Suspendisse et justo. Praesent.
      <div class="who">Marta Lins</div><div class="role">Marketing - Nome da empresa</div></div>
  </article>

  <div class="rule" style="top:876px"></div>
  <h2 class="contact-title">Fale conosco <span>agora mesmo !</span></h2>

  <div class="field" style="left:66px;top:944px;width:196px;height:26px">Digite seu nome</div>
  <div class="field" style="left:272px;top:944px;width:196px;height:26px">Digite seu email</div>
  <div class="field" style="left:66px;top:978px;width:402px;height:96px">Digite sua mensagem</div>
  <div class="send">Saiba mais</div>

  <div class="info" style="left:500px;width:120px">
    <svg width="22" height="28" viewBox="0 0 22 28"><path d="M11 1a9 9 0 0 0-9 9c0 7 9 17 9 17s9-10 9-17a9 9 0 0 0-9-9z" fill="var(--green)"/><circle cx="11" cy="10" r="3.5" fill="#fff"/></svg>
    Rua das Acácias 48<br>Bairro Jardim Alto<br>CEP 30.100-000<br>Belo Horizonte - MG
  </div>
  <div class="info" style="left:640px;width:110px">
    <svg width="28" height="28" viewBox="0 0 28 28"><circle cx="14" cy="14" r="13" fill="var(--green)"/><path d="M9 8l3-1 2 4-2 1.5c1 2 2.5 3.5 4.5 4.5L18 15l4 2-1 3c-6 0-12-6-12-12z" fill="#fff"/></svg>
    +55 31 3000-1234<br>+55 31 9000-5678
  </div>
  <div class="info" style="left:760px;width:120px">
    <svg width="30" height="24" viewBox="0 0 30 24"><rect x="1" y="2" width="28" height="20" fill="var(--green)"/><path d="M1 2l14 11L29 2" fill="none" stroke="#fff" stroke-width="2"/></svg>
    contato@orbali.com.br
  </div>

  <footer class="site-footer">
    <nav class="foot-nav"><span>HOME</span><span>A EMPRESA</span><span>TECNOLOGIA</span><span>PRODUTOS &amp; SERVIÇOS</span><span>CLIENTES &amp; PARCEIROS</span><span>CONTATO</span></nav>
    <svg class="to-top" viewBox="0 0 24 24"><path d="M12 17V8M8 11l4-4 4 4" fill="none" stroke="#fff" stroke-width="2"/></svg>
    <p class="copy">© todos os direitos reservados ORBALI.</p>
  </footer>
</div>
</body>
</html>
```